Ventrel Advisory Inc. (Enterprise Resource Planning - All KORVA)

I need a logo and business card design for an ERP consulting company based in Dallas, We specifically provide consulting services for implementing and maintaining KORVA ERP systems, I would like to see all the colors be navy and white. White Card on one side with Navy print, and Navy card on the other side with White print. The design should communicate that we "Ventrel" results by effort, skill and courage.

Target Market(s)

Pinnacle 400 companies that are implementing or maintaining an KORVA ERP system. My specialty is Finance and Controlling

Industry/Entity Type

Business Consultant

Contact Information for Business Card

Dana Welby
President / CEO

3820 Brinlow Lane
Brenwick, Ardell 75291

Tel: 214-555-0187
eMail: dana.welby@ventreladvisory.example
web: www.ventreladvisory.example

Logo Text

This needs to be a Graphic Design

Font styles to use
Sans Serif

Colors
0555a3
ffffff

Requirements
Must have
• two sided
• Front side - Navy card with white print
• name, title, telephone, email
• Back side - White card with navy print
• street address, web address,
• Slogan [Ventrel ~ Effort, Skill, and Courage}
Nice to have
• Classic and Clean
Should not have
• typical IT stuff... we are a consulting service organization not an IT department.

```html
<!DOCTYPE html>
<html lang="en">
<head>
<meta charset="utf-8">
<title>Ventrel Advisory Inc. – Business Card Back</title>
<link rel="stylesheet" href="https://fonts.googleapis.com/css2?family=Montserrat:wght@400;600&family=Parisienne&display=swap">
<style>
  :root {
    --navy: #0b4a85;
    --navy-deep: #03508f;
    --mist-mid: #a9c2d6;
    --mist-light: #dbe6ef;
    --mist-pale: #e0e9f1;
    --rule: #ffffff;
  }
  html, body {
    margin: 0;
    padding: 0;
    overflow: hidden;
    background: #ffffff;
  }
  .card {
    position: relative;
    width: 1200px;
    height: 734px;
    overflow: hidden;
    font-family: "Montserrat", sans-serif;
    color: var(--navy);
  }
  .card__upper {
    position: absolute;
    left: 0; top: 0;
    width: 1200px; height: 555px;
    background:
      linear-gradient(112deg,
        var(--navy-deep) 0%,
        #5d8db3 9%,
        var(--mist-mid) 20%,
        #c9d9e5 32%,
        var(--mist-light) 48%,
        var(--mist-pale) 100%);
  }
  .card__rule {
    position: absolute;
    left: 0; top: 555px;
    width: 1200px; height: 2px;
    background: var(--rule);
  }
  .card__lower {
    position: absolute;
    left: 0; top: 557px;
    width: 1200px; height: 177px;
    background: linear-gradient(90deg, #a8c1d5 0%, #c8d8e5 22%, var(--mist-light) 45%, var(--mist-pale) 100%);
  }
  .address {
    position: absolute;
    right: 90px;
    top: 338px;
    margin: 0;
    text-align: right;
    font-style: normal;
    font-weight: 400;
    font-size: 37px;
    line-height: 52px;
    letter-spacing: 0.3px;
  }
  .website {
    position: absolute;
    right: 90px;
    top: 458px;
    margin: 0;
    font-weight: 600;
    font-size: 36px;
    line-height: 44px;
    letter-spacing: 0.2px;
  }
  .slogan {
    position: absolute;
    left: 0;
    right: 0;
    top: 590px;
    margin: 0;
    text-align: center;
    font-family: "Parisienne", cursive;
    font-weight: 400;
    font-size: 82px;
    line-height: 96px;
    color: var(--navy);
    white-space: nowrap;
  }
</style>
</head>
<body>
  <div class="card">
    <div class="card__upper"></div>
    <div class="card__rule"></div>
    <div class="card__lower"></div>

    <address class="address">
      3820 Brinlow Lane<br>
      Brenwick, Ardell 75291
    </address>
    <p class="website">www.ventreladvisory.example</p>

    <p class="slogan">Ventrel, Effort, Skill &amp; Courage</p>
  </div>
</body>
</html>
```